Flyer-Design für Online-Schatzsuche
Zielgruppe
Der Name des Startups ist Lumora-Vex. Es handelt sich um eine Online-Schatzsuche. Irgendwo auf der Welt wird ein Schatz versteckt, der eine Million Euro wert ist. Die User registrieren sich für 19,99 Euro auf der Website und erhalten so den Zugang zu einer speziellen Seite(Quellzone), auf der wöchentlich neue Hinweise veröffentlicht werden, nachdem die Mindestanzahl an Teilnehmern (1Mio) erreicht ist. Diese Hinweise sind Rätsel aus den verschiedensten Bereichen, deren Lösungen GPS-Koordinaten und Aufenthaltsorte von weiteren Hinweisen oder dem Schatz selbst liefern.
Aufgabenstellung
Der Flyer sollte im DIN A6-Format gestaltet werden. Zudem soll er das Logo und die Domain www.lumora-vex.example enthalten. Außerdem soll der Flyer die Abenteuerlust anregen und sofort erkennbar machen, dass 1Mio Euro gewonnen werden können. Der Flyer soll später in Deutsch, Englisch, Japanisch und Mandarin vorliegen. Unter der 1Mio Euro sollte dann noch die umgerechnete Währung in amerikanischen Dollar, chinesischen Renminbi und Japanischen Yen stehen.

```html
<!DOCTYPE html>
<html lang="de">
<head>
<meta charset="utf-8">
<title>Lumora-Vex Flyer</title>
<link rel="stylesheet" href="https://fonts.googleapis.com/css2?family=Archivo+Black&family=Archivo:wght@700&display=swap">
<style>
  :root {
    --forest-light: #c9cdcb;
    --forest-mid: #7d8280;
    --forest-dark: #262a28;
    --ground: #4a3f33;
    --type-grey: #8c8c8c;
    --type-dark: #1f1f1f;
    --bar: rgba(235, 235, 235, 0.82);
    --url: #111111;
    --brand: #a7b43a;
  }
  html, body {
    margin: 0;
    padding: 0;
    overflow: hidden;
    background: #ffffff;
  }
  .flyer {
    position: relative;
    width: 851px;
    height: 1200px;
    overflow: hidden;
    font-family: "Archivo Black", "Arial Black", sans-serif;
  }
  .forest-backdrop {
    position: absolute;
    inset: 0;
    background:
      linear-gradient(180deg, rgba(0,0,0,0) 60%, var(--ground) 100%),
      linear-gradient(90deg, var(--forest-dark) 0%, var(--forest-mid) 14%, var(--forest-light) 42%, var(--forest-light) 62%, var(--forest-mid) 84%, var(--forest-dark) 100%);
  }
  .headline {
    position: absolute;
    left: 104px;
    margin: 0;
    white-space: nowrap;
    line-height: 1;
    color: transparent;
    background: linear-gradient(90deg, var(--type-grey) 0%, var(--type-grey) 18%, var(--type-dark) 50%, var(--type-grey) 82%, #b5b5b5 100%);
    -webkit-background-clip: text;
    background-clip: text;
    letter-spacing: 1px;
  }
  .line-1 { top: 128px; font-size: 78px; }
  .line-2 { top: 222px; font-size: 90px; }
  .line-3 { top: 326px; font-size: 72px; }
  .line-4 { top: 422px; font-size: 72px; }
  .line-5 { top: 530px; font-size: 84px; }
  .line-6 { top: 620px; font-size: 88px; }
  .url-bar {
    position: absolute;
    left: 103px;
    top: 755px;
    width: 645px;
    height: 48px;
    background: var(--bar);
    display: flex;
    align-items: center;
    justify-content: center;
    font-family: "Archivo", "Arial", sans-serif;
    font-weight: 700;
    font-size: 25px;
    color: var(--url);
    letter-spacing: 0.5px;
  }
  .brand {
    position: absolute;
    left: 0;
    right: 0;
    top: 1030px;
    display: flex;
    flex-direction: column;
    align-items: center;
    gap: 10px;
  }
  .brand-square {
    width: 68px;
    height: 68px;
    background: var(--brand);
  }
  .brand-name {
    font-family: "Archivo", "Arial", sans-serif;
    font-weight: 700;
    font-size: 26px;
    color: var(--brand);
  }
</style>
</head>
<body>
  <main class="flyer">
    <div class="forest-backdrop" role="img" aria-label="Nebliger Wald mit hohen, dunklen Baumstämmen und Laubboden"></div>

    <h1 class="headline line-1">Bist du ein</h1>
    <p class="headline line-2">Abenteurer?</p>
    <p class="headline line-3">Weltenbummler?</p>
    <p class="headline line-4">Ein Schatzjäger?</p>
    <p class="headline line-5">Lust auf die</p>
    <p class="headline line-6">Millionen?</p>

    <div class="url-bar">www.lumora-vex.example</div>

    <div class="brand">
      <div class="brand-square"></div>
      <div class="brand-name">Lumora-Vex</div>
    </div>
  </main>
</body>
</html>
```